Banner Ad Design for Bidmark

We are an online upscale fashion private sales site that requires banners in the following sizes and dimensions (see below). For submission, you can just submit three variations (letterheard, skyscrapper and square). The rest can be submitted later on when your design is selected. All banners can have the same look and feel or different if you feel so. They are going to be used in Plexo. So it's mandatory to abide by Plexo guidelines (Reminder given below). I have attached two files for your use, one is the company's logo and the other is one couple picture that you could use in the banner - You dont have to use them, they are material for your thoughts.

Creative Direction of Ad:
* Simple and not overly crowded
* Has a call to action (Join us, etc)
* Attention grabbing and conforms to an upscale fashion retailer (Chic & Stylish)
* Uses at least one of our unique selling proposition texts
* Informative and promotes only a visitor who is interested to click

Unique Selling Proposition:
* Private sales in Morocco
* Upscale fashion brands at -70%
* Exclusively in Morocco

IMPORTANT: Please make the banner in English but after the winner is selected, I will need the banner in French (I will provide you with the appropriate translation).

Sizes: (MAX 50K or smaller)
1. Square 250 x250
2. Small Square 200 x 189
3. Leaderboard 728 x 79
4. Sky scrapper 160x600
4. Medium Rectangle 300 x 250
5. Large Rectangle 336 x 280

(After the successful award, please also adapt the banner to add the following sizes
6. Leaderboard 468 x 60
7. Skyscrapper 120 x 600)

Winner will send the files in .Gif, JPEG, & PSD. If you have any questions, please dont hesitate to ask.

======================================================
Plexo Terms:
Ad images must be clear, recognizable, and relevant. Text appearing in the ad images must be legible. We reserve the right to disapprove low quality or blurry ad images.

Strobing, flashing backgrounds, or otherwise distracting ads are not allowed.
Your ads cannot mimic news articles and features. They may also not contain screenshots of Plexo BidLines text ads or otherwise simulate an BidLines text ad in any way.
Ads cannot pretend to be a system or site warning.
Ads cannot mimic or resemble Panels, Zed, or Orvo dialogue boxes, error message, etc.
Ads cannot have mock animated features or icons.
Ads can have an imaged button as long as the purpose of the message within the button is served or achieved through the landing page.
Specific for animated and display ad builder (template) ads:
Ads cannot have mock animated features or icons without the functionality working.

Target Market(s)

23-45 years white collard suburbans (Men & Women)

Industry/Entity Type

Fashion

Requirements
Must have
• Chic & Stylish Design.
It is not mandatory to use one of the logo file atatched but if you do not use it, please clearly display the site url (LUXE-CLUB.example)
Nice to have
• The couple picture attached but not necesarily if you have better design. I have provided two logos version (one with white and the other with black background. Use the one that suits your design best).

```html
<!DOCTYPE html>
<html lang="en">
<head>
<meta charset="utf-8">
<title>Luxe-Club banner set</title>
<link rel="stylesheet" href="https://fonts.googleapis.com/css2?family=Cinzel:wght@400;600;700&family=Tenor+Sans&display=swap">
<style>
  :root {
    --page: #ffffff;
    --panel: #2b2e31;
    --panel-light: #3a3e42;
    --gold: #e2b32a;
    --gold-light: #f6d66a;
    --gold-dark: #b9860f;
    --ink-light: #ffffff;
    --photo-warm: #7a4a32;
    --photo-dark: #3e2a22;
    --photo-light: #d9d2c8;
  }
  * { margin: 0; padding: 0; box-sizing: border-box; }
  html, body { width: 1200px; height: 900px; overflow: hidden; background: var(--page); }
  .canvas { position: relative; width: 1200px; height: 900px; }
  .banner {
    position: absolute;
    overflow: hidden;
    background: var(--panel);
    box-shadow: 0 8px 26px rgba(0,0,0,.28);
  }
  .banner svg.frame { position: absolute; inset: 0; width: 100%; height: 100%; }
  .photo { position: absolute; }
  .skyscraper { left: 137px; top: 148px; width: 160px; height: 600px; }
  .leaderboard { left: 332px; top: 148px; width: 728px; height: 79px; }
  .square { left: 332px; top: 265px; width: 250px; height: 250px; }

  .headline {
    position: absolute;
    font-family: "Tenor Sans", sans-serif;
    color: var(--ink-light);
    text-transform: uppercase;
    text-align: center;
    letter-spacing: .12em;
    line-height: 1.1;
  }
  .cta {
    position: absolute;
    font-family: "Cinzel", serif;
    font-weight: 700;
    color: var(--gold);
    text-transform: uppercase;
    letter-spacing: .06em;
    text-align: center;
    white-space: nowrap;
  }
  .site-name {
    position: absolute;
    font-family: "Cinzel", serif;
    font-weight: 600;
    color: var(--ink-light);
    text-align: center;
    white-space: nowrap;
    letter-spacing: .02em;
  }
  .tagline {
    position: absolute;
    font-family: "Cinzel", serif;
    font-weight: 700;
    color: var(--gold);
    text-transform: uppercase;
    text-align: center;
    white-space: nowrap;
    display: flex; align-items: center; justify-content: center; gap: 6px;
  }
  .tagline::before, .tagline::after {
    content: ""; height: 1px; background: var(--gold); flex: 1;
  }
  .brand-dot {
    position: absolute;
    border-radius: 50%;
    background: radial-gradient(circle at 35% 30%, var(--gold-light), var(--gold) 55%, var(--gold-dark));
  }
</style>
</head>
<body>
<main class="canvas">

  <!-- Skyscraper 160x600 -->
  <section class="banner skyscraper" aria-label="Skyscraper banner">
    <div class="photo" role="img" aria-label="Fashion photo: man in white hat and sunglasses leaning on a car door in front of a brick wall"
         style="left:0;top:40px;width:160px;height:450px;background:linear-gradient(160deg,var(--photo-warm) 0%,var(--photo-dark) 35%,var(--photo-light) 60%,#8a8580 100%);"></div>
    <svg class="frame" viewBox="0 0 160 600" aria-hidden="true">
      <defs>
        <linearGradient id="sky-gold" x1="0" x2="1">
          <stop offset="0" stop-color="var(--gold-dark)"/><stop offset=".5" stop-color="var(--gold-light)"/><stop offset="1" stop-color="var(--gold)"/>
        </linearGradient>
      </defs>
      <path d="M0 0 H160 V28 Q80 30 0 58 Z" fill="var(--panel)"/>
      <path d="M0 0 H160 V6 Q80 4 0 20 Z" fill="url(#sky-gold)"/>
      <path d="M0 600 V420 Q70 390 160 372 V600 Z" fill="var(--panel)"/>
      <path d="M160 600 H20 Q90 590 160 560 Z" fill="url(#sky-gold)"/>
    </svg>
    <div class="brand-dot" style="left:70px;top:4px;width:60px;height:60px;"></div>
    <p class="headline" style="left:0;top:418px;width:160px;font-size:15px;">Exclusive<br>deals on<br>the hottest<br>fashions</p>
    <p class="cta" style="left:0;top:510px;width:160px;font-size:11px;">Join us today at</p>
    <p class="site-name" style="left:0;top:528px;width:160px;font-size:13px;">Luxe-Club.example</p>
    <p class="tagline" style="left:4px;top:552px;width:152px;font-size:8px;">Ventes privées</p>
  </section>

  <!-- Leaderboard 728x79 -->
  <section class="banner leaderboard" aria-label="Leaderboard banner">
    <div class="photo" role="img" aria-label="Fashion photo: couple in sunglasses posing by a car in front of a brick wall"
         style="left:0;top:0;width:290px;height:79px;background:linear-gradient(90deg,var(--photo-light) 0%,var(--photo-warm) 30%,var(--photo-dark) 55%,var(--photo-light) 80%,#8a8580 100%);"></div>
    <svg class="frame" viewBox="0 0 728 79" aria-hidden="true">
      <defs>
        <linearGradient id="lb-gold" x1="0" y1="0" x2="0" y2="1">
          <stop offset="0" stop-color="var(--gold-light)"/><stop offset="1" stop-color="var(--gold-dark)"/>
        </linearGradient>
      </defs>
      <path d="M246 0 Q272 40 290 79 H728 V0 Z" fill="url(#lb-gold)"/>
      <path d="M262 0 Q284 40 300 79 H728 V0 Z" fill="var(--panel)"/>
      <path d="M700 79 Q722 60 728 30 V79 Z" fill="url(#lb-gold)"/>
    </svg>
    <div class="brand-dot" style="left:673px;top:11px;width:58px;height:58px;"></div>
    <p class="headline" style="left:280px;top:12px;width:200px;font-size:15px;line-height:1.2;">Exclusive deals<br>on the hottest<br>fashions</p>
    <p class="cta" style="left:478px;top:11px;width:186px;font-size:13px;">Join us today at</p>
    <p class="site-name" style="left:478px;top:29px;width:186px;font-size:17px;">Luxe-Club.example</p>
    <p class="tagline" style="left:492px;top:57px;width:158px;font-size:9px;">Ventes privées</p>
  </section>

  <!-- Square 250x250 -->
  <section class="banner square" aria-label="Square banner">
    <div class="photo" role="img" aria-label="Fashion photo: man in white hat and sunglasses leaning on a car door"
         style="left:0;top:0;width:250px;height:190px;background:linear-gradient(120deg,var(--photo-light) 0%,#9a8a7e 30%,var(--photo-warm) 60%,var(--photo-dark) 100%);"></div>
    <svg class="frame" viewBox="0 0 250 250" aria-hidden="true">
      <defs>
        <linearGradient id="sq-gold" x1="0" x2="1">
          <stop offset="0" stop-color="var(--gold-dark)"/><stop offset=".5" stop-color="var(--gold-light)"/><stop offset="1" stop-color="var(--gold)"/>
        </linearGradient>
      </defs>
      <path d="M150 0 H250 V26 Q210 6 150 0 Z" fill="url(#sq-gold)"/>
      <path d="M0 250 V178 Q120 162 250 132 V250 Z" fill="var(--panel)"/>
      <path d="M250 250 H120 Q200 244 250 222 Z" fill="url(#sq-gold)"/>
    </svg>
    <div class="brand-dot" style="left:194px;top:146px;width:56px;height:56px;"></div>
    <p class="headline" style="left:112px;top:24px;width:136px;font-size:16px;line-height:1.15;">Exclusive<br>deals on<br>the hottest<br>fashions</p>
    <p class="cta" style="left:10px;top:178px;width:160px;font-size:11px;">Join us today at</p>
    <p class="site-name" style="left:8px;top:196px;width:180px;font-size:15px;">Luxe-Club.example</p>
    <p class="tagline" style="left:22px;top:221px;width:172px;font-size:9px;">Ventes privées</p>
  </section>

</main>
</body>
</html>
```